Poster for a series of live music events

Looking for a simplistic poster design for live music gigs. I would like something that i can reuse by moving the positioning of the words on the poster and the colour scheme. Attached is an example of a design that i like. The size should be A4.
File format preferred would be photoshop.
Text in the poster is not that important at this stage as it is just a template i am after. But it should include band names, location, date and time. So feel free to make up the text. The file provided in the brief will show you the similar things that will be included.
Events

```html
<!DOCTYPE html>
<html lang="en">
<head>
<meta charset="utf-8">
<title>Live Music Poster Series</title>
<link rel="stylesheet" href="https://fonts.googleapis.com/css2?family=Poppins:wght@300;400;500;600&display=swap">
<style>
  :root {
    --canvas-bg: #e4e4e4;
    --white: #ffffff;
    --ink: #111111;
    --rule: rgba(255,255,255,0.85);
    --navy-top: #0a0d22;
    --navy-mid: #14193a;
    --navy-accent: #7cc4ec;
    --violet-top: #3c1f6c;
    --violet-mid: #57338f;
    --violet-accent: #c79ad8;
    --emerald-top: #0a3a25;
    --emerald-mid: #13583a;
    --emerald-accent: #8fd4ae;
  }
  * { margin: 0; padding: 0; box-sizing: border-box; }
  html, body {
    width: 1200px; height: 1000px; overflow: hidden;
    background: var(--canvas-bg);
    font-family: "Poppins", sans-serif;
  }
  .canvas { position: relative; width: 1200px; height: 1000px; }

  .poster {
    position: absolute; width: 440px; height: 625px; overflow: hidden;
    color: var(--white);
    background: radial-gradient(ellipse at 50% 20%, var(--mid) 0%, var(--top) 75%);
  }
  .poster--navy { left: 72px; top: 300px; z-index: 2; --top: var(--navy-top); --mid: var(--navy-mid); --accent: var(--navy-accent); }
  .poster--violet { left: 370px; top: 50px; z-index: 1; --top: var(--violet-top); --mid: var(--violet-mid); --accent: var(--violet-accent); }
  .poster--emerald { left: 693px; top: 217px; z-index: 2; --top: var(--emerald-top); --mid: var(--emerald-mid); --accent: var(--emerald-accent); }

  .poster__splash {
    position: absolute; left: 60px; top: 20px; width: 320px; height: 200px;
    background: radial-gradient(ellipse at 50% 50%, rgba(255,255,255,0.55) 0%, color-mix(in srgb, var(--accent) 45%, transparent) 40%, transparent 72%);
  }
  .poster__brand {
    position: absolute; left: 0; right: 0; top: 108px;
    display: flex; justify-content: center; align-items: center; gap: 12px;
    font-size: 38px; font-weight: 500; letter-spacing: 1px; color: var(--white);
  }
  .poster__brand-mark { width: 14px; height: 14px; background: var(--white); }

  .poster__present {
    position: absolute; left: 0; right: 0; top: 233px; text-align: center;
    font-size: 14px; font-weight: 300; letter-spacing: 6px;
  }
  .poster__headline {
    position: absolute; left: 0; right: 0; top: 268px; text-align: center;
    font-size: 82px; line-height: 90px; letter-spacing: -2px;
    background: linear-gradient(100deg, #f4f4f4 0%, #cfcfcf 35%, var(--accent) 60%, #e9e9e9 85%);
    -webkit-background-clip: text; background-clip: text; color: transparent;
  }
  .poster__headline-light { font-weight: 300; }
  .poster__headline-bold { font-weight: 600; }

  .poster__rule {
    position: absolute; left: 50px; width: 353px; height: 0;
    border-top: 3px dotted var(--rule);
  }
  .poster__rule--one { top: 380px; }
  .poster__rule--two { top: 456px; }
  .poster__rule--three { top: 518px; }

  .poster__location {
    position: absolute; left: 0; right: 0; top: 398px; text-align: center;
    font-size: 28px; font-weight: 300; letter-spacing: 9px;
  }
  .poster__when {
    position: absolute; left: 50px; width: 353px; top: 477px;
    display: flex; justify-content: space-between; font-size: 21px; font-weight: 300;
  }
  .poster__when strong { font-weight: 600; }
  .poster__extra {
    position: absolute; left: 50px; width: 353px; top: 535px;
    display: flex; justify-content: space-between; font-size: 12.5px; font-weight: 300;
  }
  .poster__tickets {
    position: absolute; left: 83px; top: 590px; width: 285px; height: 35px;
    background: var(--white); color: var(--ink); border-radius: 8px 8px 0 0;
    display: flex; align-items: center; justify-content: center;
    font-size: 13px; font-weight: 500;
  }
</style>
</head>
<body>
<main class="canvas">

  <article class="poster poster--violet">
    <div class="poster__splash" role="img" aria-label="Burst of white music notes behind the brand name"></div>
    <div class="poster__brand"><span class="poster__brand-mark"></span>Loudwave</div>
    <p class="poster__present">PRESENT</p>
    <h1 class="poster__headline"><span class="poster__headline-light">THE</span><span class="poster__headline-bold">BAND</span></h1>
    <div class="poster__rule poster__rule--one"></div>
    <p class="poster__location">LOCATIN</p>
    <div class="poster__rule poster__rule--two"></div>
    <p class="poster__when"><span><strong>15</strong>JUNE<strong>2015</strong></span><span>21.00</span></p>
    <div class="poster__rule poster__rule--three"></div>
    <p class="poster__extra"><span>ADDITIOAN TEXT</span><span>ADDITIOAN TEXT</span><span>ADDITIOAN TEXT</span></p>
    <div class="poster__tickets">buy tickets on the site</div>
  </article>

  <article class="poster poster--navy">
    <div class="poster__splash" role="img" aria-label="Burst of white music notes behind the brand name"></div>
    <div class="poster__brand"><span class="poster__brand-mark"></span>Loudwave</div>
    <p class="poster__present">PRESENT</p>
    <h1 class="poster__headline"><span class="poster__headline-light">THE</span><span class="poster__headline-bold">BAND</span></h1>
    <div class="poster__rule poster__rule--one"></div>
    <p class="poster__location">LOCATIN</p>
    <div class="poster__rule poster__rule--two"></div>
    <p class="poster__when"><span><strong>15</strong>JUNE<strong>2015</strong></span><span>21.00</span></p>
    <div class="poster__rule poster__rule--three"></div>
    <p class="poster__extra"><span>ADDITIOAN TEXT</span><span>ADDITIOAN TEXT</span><span>ADDITIOAN TEXT</span></p>
    <div class="poster__tickets">buy tickets on the site</div>
  </article>

  <article class="poster poster--emerald">
    <div class="poster__splash" role="img" aria-label="Burst of white music notes behind the brand name"></div>
    <div class="poster__brand"><span class="poster__brand-mark"></span>Loudwave</div>
    <p class="poster__present">PRESENT</p>
    <h1 class="poster__headline"><span class="poster__headline-light">THE</span><span class="poster__headline-bold">BAND</span></h1>
    <div class="poster__rule poster__rule--one"></div>
    <p class="poster__location">LOCATIN</p>
    <div class="poster__rule poster__rule--two"></div>
    <p class="poster__when"><span><strong>15</strong>JUNE<strong>2015</strong></span><span>21.00</span></p>
    <div class="poster__rule poster__rule--three"></div>
    <p class="poster__extra"><span>ADDITIOAN TEXT</span><span>ADDITIOAN TEXT</span><span>ADDITIOAN TEXT</span></p>
    <div class="poster__tickets">buy tickets on the site</div>
  </article>

</main>
</body>
</html>
```